Этикетка для флакона моющего средства
Задание на дизайн
Размер
82 мм × 180 мм
Опишите свою организацию или продукт и целевую аудиторию
Этикетка для серии специальных моющих средств, готовых к применению.
Например пятновыводитель для ковров, удалитель следов скотча и фломастера, очиститель ржавчины.
Наши моющие средства применяют как профессиональные уборщики (клинеры), так и «продвинутые домохозяйки».
Основная идея этикетки — современный минималистичный дизайн, отсутствие лишнего информационного шума, на домашней полке и в руках профессионала должно выглядеть как профессиональное средство, где упор на содержимое, на удобство пользования, а не на кричащую этикетку. Обратите внимание на фото, как будет выглядеть сам флакон, на который необходимо сделать этикетку, флакон белого цвета.
Этикетка содержит 3 блока — 1) название и лицевая часть 2) служебная часть (данные производителя, состав, штрих код и т. д. 3) информационная часть по применению — инструкция, перечень удаляемых загрязнений, подходящие поверхности для удаления
Текстовое содержание этикетки — в прилагаемом файле.
Обратите внимание 1) На лицевой части указывается величина pH продукта, при этом цвет этой надписи (или части оформления фронта этикетки) должен быть зеленой в случае кислотного, красной — щелочного, фиолетовый -нейтрального состава, но этот цвет не должен доминировать. 2) Информационную часть хотелось бы выполнить в виде пиктограмм и/или инфографики, там получится 3 группы информационной: «удаляет», «подходит», «применение» . Желательно чтобы в информационной части текста вообще не было, максимум пояснения к рисункам — пиктограммам.
Примеры пиктограмм и этикеток даны в приложении, но это не образцы для копирования, просто направление для творчества Вашего)
Приложите логотипы или другие материалы
Это флакон для которого необходимо разработать этикетку
Это наш логотип
Минималистичный дизайн
лаконичные пиктограммы
Это полный текст этикетки
приятный минимализм, но в нашем случае эко-тему не эксплуатируем
Это наш флакон
Комментарии и пожелания для дизайнеров
Эко тему не эксплуатируем, это для другой линейки, основной показатель здесь - эффективность.
Чтобы не было большого разноцветия в этикетке - цвета полосок в логотипе можно делать того же цвета, что и задан pH средства - то есть зеленым, фиолетовым или оранжевым.

```html
<!DOCTYPE html>
<html lang="ru">
<head>
<meta charset="utf-8">
<title>Этикетка — Универсал растворитель</title>
<link rel="stylesheet" href="https://fonts.googleapis.com/css2?family=Raleway:wght@300&family=Comfortaa:wght@400&family=Roboto+Condensed:wght@700&display=swap">
<style>
  :root {
    --page: #f1f1f1;
    --label: #ffffff;
    --ink: #4a4a4a;
    --ink-soft: #6b6b6b;
    --neutral: #d262e2;
    --icon-fill: #e6e6e6;
  }
  * { margin: 0; padding: 0; box-sizing: border-box; }
  html, body { width: 1200px; height: 1033px; overflow: hidden; background: var(--page); }
  .canvas { position: relative; width: 1200px; height: 1033px; }
  .label {
    position: absolute; left: 380px; top: 60px; width: 440px; height: 920px;
    background: var(--label);
  }
  .brand {
    position: absolute; left: 160px; top: 150px;
    display: flex; align-items: center; gap: 12px;
    font-family: "Roboto Condensed", sans-serif; font-weight: 700;
    font-size: 38px; letter-spacing: 1px; color: var(--ink);
  }
  .brand-mark { width: 16px; height: 16px; background: var(--neutral); }
  .title-block {
    position: absolute; right: 100px; top: 430px;
    text-align: right; white-space: nowrap;
  }
  .product-name {
    font-family: "Raleway", sans-serif; font-weight: 300;
    font-size: 38px; line-height: 1.1; letter-spacing: 0.5px; color: var(--ink-soft);
  }
  .product-type {
    font-family: "Comfortaa", sans-serif; font-size: 25px; line-height: 1.2;
    color: var(--neutral);
  }
  .category {
    position: absolute; left: 208px; top: 598px;
    font-family: "Roboto Condensed", sans-serif; font-weight: 700;
    font-size: 13px; line-height: 1.05; text-transform: uppercase; color: var(--ink);
    white-space: nowrap;
  }
  .category-dot {
    position: absolute; left: 196px; top: 600px; width: 8px; height: 8px;
    background: var(--neutral);
  }
  .ph-value {
    position: absolute; left: 262px; top: 645px;
    font-family: "Roboto Condensed", sans-serif; font-weight: 700;
    font-size: 20px; color: var(--neutral);
  }
  .usage-icons {
    position: absolute; left: 100px; top: 730px; display: flex; gap: 10px;
  }
  .usage-icon {
    width: 30px; height: 36px; border-radius: 5px; background: var(--icon-fill);
  }
</style>
</head>
<body>
<main class="canvas">
  <section class="label">
    <div class="brand"><span class="brand-mark"></span>ОРБИТА</div>
    <div class="title-block">
      <h1 class="product-name">УНИВЕРСАЛ</h1>
      <p class="product-type">растворитель</p>
    </div>
    <span class="category-dot"></span>
    <p class="category">Профессиональная<br>химия</p>
    <p class="ph-value">pH 7.5</p>
    <div class="usage-icons" role="img" aria-label="Пиктограммы применения: распылить, выдержать 3 минуты, протереть, смыть водой">
      <span class="usage-icon"></span>
      <span class="usage-icon"></span>
      <span class="usage-icon"></span>
      <span class="usage-icon"></span>
      <span class="usage-icon"></span>
      <span class="usage-icon"></span>
    </div>
  </section>
</main>
</body>
</html>
```